Larkmoor Institute Seminar Series Flyer

I am looking to update our Larkmoor Institute flyer. Please take a look at the our current version attached and feel free to revise as you see fit. I would like something eye catching, but not to busy. I am attaching the epigenetics logo as well. It would be great if you could use the logo and take out the white background in the logo to fit in seamlessly within the flyer.

Target Market(s)

Medical Doctors and Scientist

```html
<!DOCTYPE html>
<html lang="en">
<head>
<meta charset="utf-8">
<title>Larkmoor Institute Seminar Series</title>
<link rel="stylesheet" href="https://fonts.googleapis.com/css2?family=Tinos:ital,wght@0,400;0,700;1,400&display=swap">
<style>
  :root{
    --navy:#0d3a82;
    --blue:#1f5cb4;
    --sky:#6f9ddc;
    --pale:#dce8f7;
    --red:#b4202a;
    --ink:#1b2a4a;
    --paper:#ffffff;
  }
  *{box-sizing:border-box;margin:0;padding:0}
  html,body{width:800px;height:1200px;overflow:hidden;background:var(--paper)}
  body{font-family:"Tinos","Times New Roman",serif;color:var(--ink)}
  .flyer{position:relative;width:800px;height:1200px;overflow:hidden;background:var(--paper)}
  .header-art{position:absolute;left:0;top:0;width:800px;height:320px}
  .brand{position:absolute;left:60px;top:62px;display:flex;align-items:center;gap:12px}
  .brand-dot{width:22px;height:22px;border-radius:50%;background:var(--red)}
  .brand-name{font-size:26px;font-weight:700;color:var(--navy)}
  .masthead{position:absolute;left:60px;top:312px}
  .masthead-title{font-size:50px;font-weight:700;color:var(--navy);letter-spacing:1px;line-height:1}
  .masthead-sub{margin-top:10px;font-size:20px;color:var(--red);font-variant:small-caps;letter-spacing:2px}
  .program{position:absolute;left:80px;right:80px;top:460px;text-align:center}
  .speaker{font-size:28px;font-weight:700;color:var(--navy)}
  .affiliation{margin-top:12px;font-size:19px;color:var(--navy);text-transform:uppercase;line-height:1.35;letter-spacing:.5px}
  .talk{margin-top:16px;font-size:27px;color:var(--red);line-height:1.25}
  .second{margin-top:58px}
  .speaker-minor{font-size:24px}
  .when{margin-top:66px;font-size:26px;font-weight:700;color:var(--navy)}
  .where{margin-top:10px;font-size:24px;color:var(--navy)}
  .footer{position:absolute;left:0;bottom:0;width:800px;height:110px;background:linear-gradient(90deg,var(--navy),var(--blue));display:flex;align-items:center;justify-content:space-between;padding:0 60px}
  .footer-note{color:#fff;font-size:14px;line-height:1.45;max-width:420px}
  .footer-brand{display:flex;align-items:center;gap:10px}
  .footer-square{width:18px;height:18px;background:#fff}
  .footer-name{color:#fff;font-size:28px;font-weight:700}
</style>
</head>
<body>
<main class="flyer">
  <svg class="header-art" viewBox="0 0 800 320">
    <defs>
      <linearGradient id="bandFill" x1="1" y1="0" x2="0" y2="1">
        <stop offset="0" stop-color="#0d3a82"/>
        <stop offset=".55" stop-color="#2a6cc4"/>
        <stop offset="1" stop-color="#9fc0ea"/>
      </linearGradient>
      <radialGradient id="helixGlow" cx=".7" cy=".3" r=".6">
        <stop offset="0" stop-color="#ffffff" stop-opacity=".14"/>
        <stop offset="1" stop-color="#ffffff" stop-opacity="0"/>
      </radialGradient>
      <clipPath id="bandClip">
        <path d="M330 0 H800 V262 C620 205 420 185 0 196 V168 C200 150 300 90 330 0 Z"/>
      </clipPath>
    </defs>
    <path d="M330 0 H800 V262 C620 205 420 185 0 196 V168 C200 150 300 90 330 0 Z" fill="url(#bandFill)"/>
    <rect x="400" y="0" width="400" height="262" fill="url(#helixGlow)" clip-path="url(#bandClip)" role="img" aria-label="Faint double helix graphic across the blue header band"/>
    <path d="M0 210 C420 198 620 220 800 276" fill="none" stroke="#dce8f7" stroke-width="10"/>
    <path d="M0 224 C420 212 620 234 800 290" fill="none" stroke="#6f9ddc" stroke-width="2"/>
  </svg>

  <div class="brand">
    <span class="brand-dot"></span>
    <span class="brand-name">Larkmoor</span>
  </div>

  <header class="masthead">
    <h1 class="masthead-title">LARKMOOR INSTITUTE</h1>
    <p class="masthead-sub">Seminar Series</p>
  </header>

  <section class="program">
    <p class="speaker">Adrian M Calloway, Ph.D.</p>
    <p class="affiliation">Assistant Professor of Genetics Ashgrove School of<br>Medicine at the University of Hollinbrook</p>
    <p class="talk">Dissecting the molecular basis of chromosome<br>positioning</p>

    <div class="second">
      <p class="speaker speaker-minor">Nora Veltkamp, (Sorel Lab)</p>
      <p class="talk">Exploiting Dna Deaminases To Localize<br>5-Hydroxymethylcytosine In The Genome</p>
    </div>

    <p class="when">Thursday, March 9, 2017 @ 4 PM</p>
    <p class="where">9-146 Ashdown Center</p>
  </section>

  <footer class="footer">
    <p class="footer-note">Seminars are open to all faculty, staff and students. For more details visit our institute office.</p>
    <div class="footer-brand">
      <span class="footer-square"></span>
      <span class="footer-name">Hollinbrook</span>
    </div>
  </footer>
</main>
</body>
</html>
```